lawn sign

Lawn Sign
Roofing Gutters Windows

Target Market(s)

roofing

Font styles to use
Sans Serif

Colors
86cfc6
33a6d7
fbee3f
faa54b

Requirements
Must have
• my logo
Nice to have
• designer for now

```html
<!DOCTYPE html>
<html lang="en">
<head>
<meta charset="utf-8">
<title>Lawn Sign – Roofing Gutters Windows</title>
<link rel="stylesheet" href="https://fonts.googleapis.com/css2?family=EB+Garamond:wght@500&display=swap">
<style>
  :root {
    --orange: #faa54b;
    --yellow: #fbee3f;
    --white: #ffffff;
    --sky: #33a6d7;
    --mint: #86cfc6;
  }
  html, body {
    margin: 0;
    padding: 0;
    width: 1200px;
    height: 800px;
    overflow: hidden;
    background: var(--white);
  }
  .lawn-sign {
    position: relative;
    width: 1200px;
    height: 800px;
    overflow: hidden;
    font-family: "EB Garamond", Georgia, serif;
  }
  .sign-waves {
    position: absolute;
    inset: 0;
    width: 1200px;
    height: 800px;
  }
  .wave-orange { fill: var(--orange); }
  .wave-yellow { fill: var(--yellow); }
  .wave-white  { fill: var(--white); }

  .brand {
    position: absolute;
    left: 0;
    right: 0;
    top: 250px;
    height: 150px;
    display: flex;
    align-items: center;
    justify-content: center;
    gap: 32px;
  }
  .brand-mark {
    flex: none;
    width: 130px;
    height: 130px;
    border-radius: 50%;
    background: var(--mint);
  }
  .brand-name {
    margin: 0;
    color: var(--sky);
    font-weight: 500;
    font-size: 56px;
    line-height: 1;
    white-space: nowrap;
  }

  .services {
    position: absolute;
    left: 0;
    right: 0;
    top: 460px;
    margin: 0;
    text-align: center;
    color: var(--sky);
    font-weight: 500;
    font-size: 104px;
    line-height: 1;
    letter-spacing: 0.5px;
    white-space: nowrap;
  }
</style>
</head>
<body>
  <main class="lawn-sign">
    <svg class="sign-waves" viewBox="0 0 1200 800" aria-hidden="true">
      <rect class="wave-orange" x="0" y="0" width="1200" height="800"/>
      <path class="wave-yellow" d="M0 31 C 300 15, 700 40, 1200 146 L 1200 660 C 1000 790, 600 740, 0 654 Z"/>
      <path class="wave-white" d="M0 211 C 200 150, 420 130, 700 145 C 900 155, 1050 175, 1200 197 L 1200 595 C 1000 670, 800 680, 600 666 C 350 648, 150 625, 0 608 Z"/>
    </svg>

    <div class="brand">
      <span class="brand-mark" aria-hidden="true"></span>
      <p class="brand-name">Halvern Home Renewal Co.</p>
    </div>

    <h1 class="services">Roofing Gutters Windows</h1>
  </main>
</body>
</html>
```